Food item ad for Copper Lantern Restaurant

We need visual appealing poster for our restaurant food items, for 6 categories.
1. kebabs
-tandoori chicken tikka
- tandoori 1/2 chicken
-chicken seekh
- Chaplee chicken
- Multani lamb
- lamb bouti
- lamb chops
2. Meat lover gravy dishes
- Kadai chicken masala
- butter chicken boneless
- butter chicken
- Multani kofta curry
- lamb curry
- afghani haryali lamb
3. Try this @ Copper lantern
- lamb Palou
- keema mantu
- meat thali
- kebob wraps
- chicken rolls
- sweet rice
- keema lasagna
- Romani roti
4. For vegetarian lovers
- 8 or 9 items pick n choose thali
- vegitarian
- vegitarian mantu
- aloo tikki cholay
- aloo tikki burger
- vada pav
- pav bhaji
- mix veg pakoras
5. Snakers
- sweet BBQ corn on the cob
- cassava fried
- cassava baked
- bhel puri
- sev puri
- chaat papri
- pain puri
6. Hot n cold
- Kashmiri tea. Mango milk shake
- Indian masala tea. Lessi
- English tea. Fresh juices
- green tea Fresh lime soda
- Indian style coffee Mint lime soda
We need six poster 1 for each category
it can be simple and similar theme in all six posters
the idea is to introduce the menu from my 2 Feet x 4 feet poster hanging from the window
facing the street
you go to the website:
pls take out 8-9 items in vegetarian lovers and also the word vegetarian
Industry/Entity Type
Restaurant
Requirements
Must have
- Copper lantern chef logo attached
Some food graphics
- kebabs
- rice
- Romani roti
-Naan
Kitchen equipment graphics
- tandoor ( Indian clay oven )
-Grill
Fire, charcoal, spice ,lime etc
Copper lantern color theme ,,,,,see attachments
food item names to give customer info about the menu

```html
<!DOCTYPE html>
<html lang="en">
<head>
<meta charset="utf-8">
<title>Copper Lantern – Meat Lover Gravy Dishes</title>
<link rel="stylesheet" href="https://fonts.googleapis.com/css2?family=Allura&family=Montserrat:wght@600;700&family=Jost:wght@400;600&display=swap">
<style>
  :root {
    --paper: #ffffff;
    --paper-shade: #e9eaec;
    --ink: #161616;
    --menu-ink: #1f1f1f;
    --brand-red: #d0141c;
    --rule: #8c8c8c;
    --footer: #0c0c0c;
    --footer-ink: #ffffff;
    --wok-dark: #4a4a4c;
    --wok-mid: #7a6a55;
    --veg-green: #6f8f4a;
    --gravy: #7a3a2c;
    --curry: #dca43c;
    --rice: #f1ece2;
  }
  * { box-sizing: border-box; margin: 0; padding: 0; }
  html, body { width: 1200px; height: 2400px; overflow: hidden; }
  body {
    position: relative;
    background: radial-gradient(ellipse 80% 45% at 50% 35%, var(--paper) 0%, var(--paper) 40%, var(--paper-shade) 100%);
    font-family: "Jost", sans-serif;
    color: var(--ink);
  }
  .wok-photo {
    position: absolute; top: 0; width: 400px; height: 400px;
    background: radial-gradient(ellipse 70% 65% at 35% 35%, var(--veg-green) 0%, var(--wok-mid) 35%, var(--wok-dark) 60%, rgba(200,200,204,0.6) 85%, rgba(255,255,255,0) 100%);
  }
  .wok-photo--left { left: 0; }
  .wok-photo--right { right: 0; transform: scaleX(-1); }
  .brand {
    position: absolute; top: 390px; left: 0; width: 1200px;
    display: flex; justify-content: center; align-items: center; gap: 20px;
  }
  .brand-dot { width: 34px; height: 34px; border-radius: 50%; background: var(--brand-red); }
  .brand-name {
    font-family: "Jost", sans-serif; font-weight: 600; font-size: 56px;
    letter-spacing: 0.06em; color: var(--ink);
  }
  .chili-decor {
    position: absolute; top: 770px; width: 150px; height: 110px;
    background: radial-gradient(ellipse at center, rgba(0,0,0,0.07), transparent 70%);
  }
  .chili-decor--left { left: 30px; }
  .chili-decor--right { right: 30px; }
  .headline {
    position: absolute; top: 720px; left: 0; width: 1200px; text-align: center;
    font-family: "Allura", cursive; font-weight: 400; font-size: 250px; line-height: 1;
    color: var(--brand-red);
  }
  .subhead {
    position: absolute; top: 912px; right: 120px;
    font-family: "Montserrat", sans-serif; font-weight: 700; font-size: 50px;
    letter-spacing: 0.36em; color: var(--ink);
  }
  .double-rule {
    position: absolute; left: 50%; transform: translateX(-50%);
    height: 12px; border-top: 2px solid var(--rule); border-bottom: 2px solid var(--rule);
  }
  .double-rule--top { top: 1100px; width: 656px; }
  .double-rule--bottom { top: 1484px; width: 372px; }
  .menu-list {
    position: absolute; top: 1154px; left: 0; width: 1200px;
    list-style: none; text-align: center;
    font-size: 43px; line-height: 49px; text-transform: uppercase; color: var(--menu-ink);
  }
  .dish-photo {
    position: absolute; top: 1620px; left: 0; width: 1200px; height: 664px;
    background: linear-gradient(180deg, rgba(255,255,255,0) 0%, #d9d4cf 14%, var(--gravy) 30%, #cfc8c0 44%, var(--curry) 62%, #e6c27a 80%, var(--rice) 100%);
  }
  .footer {
    position: absolute; bottom: 0; left: 0; width: 1200px; height: 116px;
    background: var(--footer); color: var(--footer-ink);
    display: flex; align-items: center; justify-content: center;
    font-family: "Montserrat", sans-serif; font-weight: 700; font-size: 40px; letter-spacing: 0.03em;
  }
</style>
</head>
<body>
  <div class="wok-photo wok-photo--left" role="img" aria-label="Photo of a wok tossing stir-fried vegetables and mushrooms"></div>
  <div class="wok-photo wok-photo--right" role="img" aria-label="Photo of a wok tossing stir-fried vegetables and mushrooms"></div>

  <div class="brand">
    <span class="brand-dot"></span>
    <span class="brand-name">COPPER LANTERN</span>
  </div>

  <div class="chili-decor chili-decor--left" role="img" aria-label="Faint chilli pepper decoration"></div>
  <div class="chili-decor chili-decor--right" role="img" aria-label="Faint chilli pepper decoration"></div>

  <h1 class="headline">Meat lover</h1>
  <h2 class="subhead">GRAVY DISHES</h2>

  <div class="double-rule double-rule--top"></div>
  <ul class="menu-list">
    <li>Kadai Chicken Masala</li>
    <li>Butter Chicken Boneless</li>
    <li>Butter Chicken</li>
    <li>Multani Kofta Curry</li>
    <li>Lamb Curry</li>
    <li>Afghani Haryali Lamb</li>
  </ul>
  <div class="double-rule double-rule--bottom"></div>

  <div class="dish-photo" role="img" aria-label="Photo of two gravy boats of curry sauce behind a plate of chicken curry on white rice"></div>

  <footer class="footer">WWW.MYCOPPERLANTERN.COM</footer>
</body>
</html>
```